Coffee and hot drinks advert on A-Board

Creative eye catching design to advertise coffee and hot drinks on an A-Board.

To use images and modern design to reflect the quality and almost specialist coffee house style drinks on offer.
We use organic milk and have had our own 'Millbrook Restaurant' coffee beans roasted to produce the perfect coffee.
We also use only the best hot chocolate and fresh cream to serve quality drinks.
All staff are barista trained.

Target Market(s)

Passing trade and coffee lovers for takeaway drinks

Industry/Entity Type

Coffee Shop

Font styles to use
Serif

Requirements
Must have
• Bold creative modern look.
• Independent coffee shop style look
• Mention we use 'Heron Organic milk'
• We use our own roasted special blend of coffee
• speciality hot chocolate
Nice to have
• modern approach
• eye catching
Should not have
• complicated
• difficult to read
• old fashioned

```html
<!DOCTYPE html>
<html lang="en">
<head>
<meta charset="utf-8">
<title>Organic Milk Coffee Advert</title>
<link rel="stylesheet" href="https://fonts.googleapis.com/css2?family=Lobster&family=Roboto+Condensed:ital,wght@0,300;0,400;1,300&display=swap">
<style>
  :root {
    --paper: #ffffff;
    --accent-orange: #f7901e;
    --headline-orange: #f9a21b;
    --roast-dark: #4a2208;
    --roast-mid: #7a3f12;
    --roast-light: #9c5a22;
    --rule: rgba(60, 28, 6, 0.6);
    --url-grey: #555555;
  }
  * { margin: 0; padding: 0; box-sizing: border-box; }
  html, body {
    width: 1200px;
    height: 933px;
    overflow: hidden;
    background: var(--paper);
  }
  .advert {
    position: relative;
    width: 1200px;
    height: 933px;
    overflow: hidden;
    background: var(--paper);
  }
  .advert__shapes {
    position: absolute;
    inset: 0;
  }
  .logo-box {
    position: absolute;
    left: 802px;
    top: 0;
    width: 283px;
    height: 218px;
    background: var(--paper);
    border-radius: 0 0 12px 12px;
    display: flex;
    align-items: flex-end;
    justify-content: center;
    padding-bottom: 24px;
  }
  .logo-box__name {
    font-family: "Roboto Condensed", sans-serif;
    font-weight: 300;
    font-size: 50px;
    color: var(--headline-orange);
    line-height: 1;
  }
  .headline {
    font-family: "Lobster", cursive;
    font-weight: 400;
  }
  .headline__lead,
  .headline__main {
    position: absolute;
    left: 670px;
    width: 520px;
    text-align: center;
    line-height: 1;
    white-space: nowrap;
  }
  .headline__lead {
    top: 250px;
    font-size: 146px;
    color: var(--headline-orange);
  }
  .headline__main {
    top: 388px;
    font-size: 96px;
    color: var(--paper);
  }
  .rule {
    position: absolute;
    left: 697px;
    width: 503px;
    height: 1px;
    background: var(--rule);
  }
  .rule--top { top: 502px; }
  .rule--bottom { top: 677px; }
  .story {
    position: absolute;
    left: 697px;
    top: 520px;
    width: 480px;
    font-family: "Roboto Condensed", sans-serif;
    font-style: italic;
    font-weight: 300;
    font-size: 29px;
    line-height: 45px;
    color: var(--paper);
    white-space: nowrap;
  }
  .website {
    position: absolute;
    right: 36px;
    top: 864px;
    font-family: "Roboto Condensed", sans-serif;
    font-weight: 300;
    font-size: 28px;
    line-height: 1;
    letter-spacing: 17px;
    color: var(--url-grey);
  }
</style>
</head>
<body>
  <main class="advert">
    <svg class="advert__shapes" width="1200" height="933" viewBox="0 0 1200 933" xmlns="http://www.w3.org/2000/svg">
      <defs>
        <linearGradient id="photoTone" x1="0" y1="0" x2="1" y2="1">
          <stop offset="0" stop-color="#e9e4de"/>
          <stop offset="0.35" stop-color="#b9977a"/>
          <stop offset="0.7" stop-color="#5a3016"/>
          <stop offset="1" stop-color="#2e1608"/>
        </linearGradient>
        <radialGradient id="roastTone" cx="0.45" cy="0.35" r="0.8">
          <stop offset="0" stop-color="var(--roast-light)"/>
          <stop offset="0.5" stop-color="var(--roast-mid)"/>
          <stop offset="1" stop-color="var(--roast-dark)"/>
        </radialGradient>
      </defs>
      <polygon class="photo-panel" role="img" aria-label="Photograph of a white cup of black coffee on a saucer surrounded by roasted coffee beans on burlap"
               points="0,0 446,0 630,465 446,933 0,933" fill="url(#photoTone)"/>
      <polygon class="chevron-stripe" points="455,0 485,0 669,465 485,933 455,933 639,465" fill="var(--accent-orange)"/>
      <path class="roast-band" role="img" aria-label="Warm brown coffee backdrop with soft latte swirl and beans"
            d="M492,0 H1200 V690 C1180,700 1170,730 1150,740 C1120,760 1110,815 1075,820 C1040,825 1030,780 1000,770 C970,760 960,800 930,800 C900,800 900,760 870,745 C840,735 830,760 800,752 C770,745 760,720 730,722 C700,724 690,745 660,735 C630,725 610,700 580,692 L674,465 Z"
            fill="url(#roastTone)"/>
    </svg>

    <div class="logo-box">
      <span class="logo-box__name">Logo area</span>
    </div>

    <h1 class="headline">
      <span class="headline__lead">We use</span>
      <span class="headline__main">organic milk</span>
    </h1>

    <div class="rule rule--top"></div>
    <p class="story">We have our own 'Millbrook Restaurant'<br>coffee beans roasted to produce the<br>perfect coffee.</p>
    <div class="rule rule--bottom"></div>

    <p class="website">www.yourwebsite.com</p>
  </main>
</body>
</html>
```